Website setup with Velmor works (childtheme is tallow theme)

hey there, my name is tobin and i would need a website. Korvel Framework, I use the tallow theme. I would like to say goodbye to the eye-catching website with a nice menu. I like to send you some example from websites I like. Https://dunmarrowcraft.com/about/ https://dunmarrowcraft.com The main tabs on the top should be "About", "Blog", "Video", "Resources" on the right / blog /

1 page

0493ce
fbee3d
faa54b

```html
<!DOCTYPE html>
<html lang="en">
<head>
<meta charset="utf-8">
<title>Tobin Life</title>
<link rel="stylesheet" href="https://fonts.googleapis.com/css2?family=Oswald:wght@600;700&family=Roboto:wght@400;500;700;900&display=swap">
<style>
:root{
  --orange:#e8501a;
  --dark:#1a1a1a;
  --footer:#2a2625;
  --text:#555;
  --heading:#1e1e1e;
  --white:#fff;
  --red:#d8161c;
  --fb:#2b4c9b;
  --ig:#355c86;
  --tw:#1f8cec;
  --blue:#1a5fc2;
  --green:#5fa52f;
}
*{margin:0;padding:0;box-sizing:border-box}
html,body{width:1200px;height:3681px;overflow:hidden}
body{position:relative;font-family:"Roboto",Arial,sans-serif;color:var(--text);background:var(--white)}
.abs{position:absolute}
/* nav */
.site-nav{left:0;top:0;width:1200px;height:100px;background:var(--dark);display:flex;align-items:center;justify-content:space-between;padding:0 132px 0 130px}
.brand{font-size:36px;font-weight:700;color:var(--white)}
.menu{display:flex;gap:28px;align-items:center;list-style:none;color:var(--white);font-size:17px;font-weight:500}
/* hero */
.hero{left:0;top:100px;width:1200px;height:577px;background:linear-gradient(100deg,#c9c3bb 0%,#a8a096 40%,#4a3f38 70%,#6b5d52 100%)}
.hero-title{left:165px;top:295px;font-family:"Oswald",sans-serif;font-weight:700;font-size:64px;line-height:72px;color:var(--orange);-webkit-text-stroke:2px var(--white);text-transform:uppercase}
.play{left:548px;top:304px}
.slide-arrow{width:32px;height:32px;border-radius:50%;background:#111;top:354px}
/* welcome */
.welcome-bg{left:0;top:677px;width:1200px;height:525px;background:linear-gradient(90deg,#e2e0dc,#f2f1ef)}
.welcome-photo{left:123px;top:690px;width:466px;height:512px;background:linear-gradient(180deg,#cdb8a2 0%,#b39276 35%,#2e4e9a 60%,#2a4690 100%);border-radius:200px 200px 0 0}
.welcome-title{left:601px;top:790px;font-size:38px;font-weight:900;color:var(--heading)}
.welcome-title span{color:var(--orange)}
.welcome-text{left:601px;top:855px;width:470px;font-size:14px;line-height:26px}
.btn{display:inline-block;background:var(--orange);color:var(--white);font-size:14px;font-weight:700;text-transform:uppercase;padding:10px 17px}
/* social stats */
.stats{left:130px;top:1178px;width:937px;height:86px;display:flex}
.stat{flex:1;display:flex;align-items:center;gap:22px;padding-left:22px;color:var(--white)}
.stat .mark{width:30px;height:30px;border-radius:50%;background:rgba(255,255,255,.9)}
.stat b{display:block;font-size:26px;font-weight:700}
.stat small{font-size:9px;letter-spacing:1px;opacity:.8}
/* section headings */
.sec-title{left:0;width:1200px;text-align:center;font-size:38px;font-weight:700;color:var(--heading)}
.sec-rule{left:540px;width:120px;height:2px;background:var(--orange)}
/* services */
.card{top:1472px;width:285px;height:344px;color:var(--white);text-align:center;padding:40px 30px 0}
.card h3{font-size:17px;font-weight:700;margin:20px 0 14px;text-transform:uppercase}
.card p{font-size:11.5px;line-height:21px}
.card .more{display:inline-block;margin-top:24px;border:2px solid var(--white);border-radius:20px;padding:6px 16px;font-size:11px;font-weight:700;text-transform:uppercase}
.card.mid{box-shadow:0 10px 25px rgba(0,0,0,.3)}
/* difference */
.diff-photo{left:0;top:1914px;width:1200px;height:528px;background:linear-gradient(90deg,#f6f6f6 0%,#f1f1f1 30%,#a9b4c0 50%,#7f8a99 70%,#c8d2dc 100%)}
.diff-title{left:132px;top:2050px;font-size:50px;line-height:56px;font-weight:900;color:var(--heading);text-transform:uppercase}
.diff-title span{color:var(--orange)}
.diff-text{left:132px;top:2178px;width:400px;font-size:14px;line-height:24px}
/* posts */
.post{top:2670px;width:292px;text-align:center}
.post .thumb{height:182px;background:linear-gradient(135deg,#8a8f99,#3e4552)}
.post .date{width:60px;height:60px;border-radius:50%;background:var(--orange);color:var(--white);font-size:10px;font-weight:700;line-height:14px;margin:-30px auto 0;padding-top:16px;position:relative}
.post h4{font-size:18px;font-weight:500;color:var(--heading);margin:6px 0 12px}
.post p{font-size:11.5px;line-height:20px;padding:0 4px}
.post hr{border:0;height:2px;background:#888;margin-top:22px}
/* footer */
.footer{left:0;top:3150px;width:1200px;height:531px}
.news-title{left:132px;top:3233px;font-size:22px;font-weight:700;color:var(--white);text-transform:uppercase}
.news-sub{left:132px;top:3265px;font-size:12px;color:#ddd}
.news-input{left:530px;top:3239px;width:248px;height:40px;background:var(--white);font-size:12px;color:#777;padding:12px 14px}
.news-btn{left:778px;top:3239px;width:112px;height:40px;background:var(--orange);color:var(--white);font-size:12px;font-weight:700;text-align:center;line-height:40px}
.soc{width:20px;height:20px;border-radius:50%;background:#6e6a68}
.f-head{top:3372px;font-size:17px;font-weight:700;color:var(--white);text-transform:uppercase}
.f-about{left:132px;top:3408px;width:470px;font-size:12px;line-height:23px;color:#ddd}
.f-contact{left:690px;top:3418px;list-style:none;font-size:12px;line-height:18px;color:#ddd}
.f-contact li{display:flex;gap:12px;margin-bottom:14px}
.f-links{left:956px;top:3412px;list-style:none;font-size:12px;line-height:24px;color:#ddd}
.f-links li::before{content:"›";margin-right:8px}
.copy{left:0;top:3632px;width:1200px;text-align:center;font-size:11px;color:#ddd}
</style>
</head>
<body>

<header class="site-nav abs">
  <div class="brand">Tobin Life</div>
  <ul class="menu">
    <li>HOME</li><li>ABOUT</li><li>BLOG</li><li>VIDEO</li><li>RESOURCES</li><li>CONTACT</li>
    <li><svg width="16" height="16" viewBox="0 0 16 16"><circle cx="6.5" cy="6.5" r="4.5" fill="none" stroke="#fff" stroke-width="2"/><line x1="10" y1="10" x2="14" y2="14" stroke="#fff" stroke-width="2"/></svg></li>
  </ul>
</header>

<section class="hero abs" role="img" aria-label="Speaker presenting at a podium to a seated audience in a bright conference hall"></section>
<h1 class="hero-title abs">I'm an online<br>marketer</h1>
<svg class="play abs" width="96" height="96" viewBox="0 0 96 96"><circle cx="48" cy="48" r="42" fill="none" stroke="#fff" stroke-width="7"/><polygon points="38,28 68,48 38,68" fill="#fff"/></svg>
<div class="slide-arrow abs" style="left:98px"><svg width="32" height="32"><polyline points="19,10 13,16 19,22" fill="none" stroke="#fff" stroke-width="2.5"/></svg></div>
<div class="slide-arrow abs" style="left:1062px"><svg width="32" height="32"><polyline points="13,10 19,16 13,22" fill="none" stroke="#fff" stroke-width="2.5"/></svg></div>

<section class="welcome-bg abs"></section>
<div class="welcome-photo abs" role="img" aria-label="Portrait of a bearded man in a blue t-shirt"></div>
<h2 class="welcome-title abs">WELCOME TO <span>TOBIN LIFE</span></h2>
<div class="welcome-text abs">
  <p>Sed ut perspiciatis unde omnis iste natus error sit voluptatem accusantium doloremque laudantium, totam rem aperiam, eaque ipsa quae ab illo inventore veritatis et quasi architecto beatae vitae dicta sunt explicabo. Nemo enim ipsam voluptatem quia voluptas sit aspernatur aut odit aut fugit, sed quia consequuntur magni dolores eos qui ratione voluptatem sequi nesciunt. Neque porro quisquam est, qui dolorem</p>
  <span class="btn" style="margin-top:26px">Read more</span>
</div>

<div class="stats abs">
  <div class="stat" style="background:var(--red)"><span class="mark"></span><div><b>519.3K</b><small>FANS</small></div></div>
  <div class="stat" style="background:var(--fb)"><span class="mark"></span><div><b>72.7K</b><small>LIKES</small></div></div>
  <div class="stat" style="background:var(--ig)"><span class="mark"></span><div><b>60.9K</b><small>FOLLOWERS</small></div></div>
  <div class="stat" style="background:var(--tw)"><span class="mark"></span><div><b>19.8K</b><small>FOLLOWERS</small></div></div>
</div>

<h2 class="sec-title abs" style="top:1342px">MY SERVICES</h2>
<div class="sec-rule abs" style="top:1415px"></div>

<div class="card abs" style="left:140px;background:var(--blue)">
  <svg width="62" height="58" viewBox="0 0 62 58" fill="none" stroke="#fff" stroke-width="2.5"><rect x="22" y="4" width="36" height="24"/><circle cx="12" cy="20" r="6"/><path d="M2 44v-8a10 10 0 0 1 20 0v8"/><circle cx="32" cy="40" r="4"/><circle cx="48" cy="40" r="4"/><path d="M24 56a8 8 0 0 1 16 0M40 56a8 8 0 0 1 16 0"/></svg>
  <h3>Business coach</h3>
  <p>Sed ut perspiciatis unde omnis iste natus error sit voluptatem accusantium doloremque laudantium, totam rem aperiam, eaque ipsa quae ab illo inventore</p>
  <span class="more">Read more</span>
</div>
<div class="card mid abs" style="left:456px;background:var(--orange)">
  <svg width="62" height="58" viewBox="0 0 62 58" fill="none" stroke="#fff" stroke-width="2.5"><path d="M31 56V20"/><path d="M31 34c-8 0-14-6-14-14 8 0 14 6 14 14zM31 28c8 0 14-6 14-14-8 0-14 6-14 14z"/><circle cx="31" cy="8" r="4"/><path d="M20 56h22"/></svg>
  <h3>Life coach</h3>
  <p>Sed ut perspiciatis unde omnis iste natus error sit voluptatem accusantium doloremque laudantium, totam rem aperiam, eaque ipsa quae ab illo inventore</p>
  <span class="more">Read more</span>
</div>
<div class="card abs" style="left:775px;background:var(--green)">
  <svg width="62" height="58" viewBox="0 0 62 58" fill="none" stroke="#fff" stroke-width="2.5"><rect x="6" y="14" width="50" height="36"/><path d="M6 14l25 20 25-20"/><path d="M31 2v6M20 5l3 5M42 5l-3 5"/></svg>
  <h3>Online market</h3>
  <p>Sed ut perspiciatis unde omnis iste natus error sit voluptatem accusantium doloremque laudantium, totam rem aperiam, eaque ipsa quae ab illo inventore</p>
  <span class="more">Read more</span>
</div>

<section class="diff-photo abs" role="img" aria-label="Team of colleagues gathered around a laptop in a bright office"></section>
<h2 class="diff-title abs">Let's make<br><span>a difference</span></h2>
<div class="diff-text abs">
  <p>Sed ut perspiciatis unde omnis iste natus error sit voluptatem accusantium doloremque laudantium, totam rem aperiam, eaque ipsa quae ab illo inventore veritatis et quasi architecto</p>
  <span class="btn" style="margin-top:24px">Read more</span>
</div>

<h2 class="sec-title abs" style="top:2527px">MOST RECENT POSTS</h2>
<div class="sec-rule abs" style="top:2605px"></div>

<article class="post abs" style="left:132px">
  <div class="thumb" role="img" aria-label="Business team meeting around a table"></div>
  <div class="date">APR 05<br>2018</div>
  <h4>Nemo enim ipsam voluptatem</h4>
  <p>Sed ut perspiciatis unde omnis iste natus error sit voluptatem accusantium doloremque laudantium, totam rem aperiam, eaque ipsa quae ab illo inventore veritatis et quasi architecto beatae vitae dicta</p>
  <hr>
</article>
<article class="post abs" style="left:454px">
  <div class="thumb" role="img" aria-label="Businesswoman seated in an office" style="background:linear-gradient(135deg,#6b4a32,#2f2a28)"></div>
  <div class="date">APR 05<br>2018</div>
  <h4>Nemo enim ipsam voluptatem</h4>
  <p>Sed ut perspiciatis unde omnis iste natus error sit voluptatem accusantium doloremque laudantium, totam rem aperiam, eaque ipsa quae ab illo inventore veritatis et quasi architecto beatae vitae dicta</p>
  <hr>
</article>
<article class="post abs" style="left:773px">
  <div class="thumb" role="img" aria-label="Group of coworkers collaborating at a desk" style="background:linear-gradient(135deg,#c9ccd4,#6a7590)"></div>
  <div class="date">APR 05<br>2018</div>
  <h4>Nemo enim ipsam voluptatem</h4>
  <p>Sed ut perspiciatis unde omnis iste natus error sit voluptatem accusantium doloremque laudantium, totam rem aperiam, eaque ipsa quae ab illo inventore veritatis et quasi architecto beatae vitae dicta</p>
  <hr>
</article>

<svg class="footer abs" width="1200" height="531" viewBox="0 0 1200 531" preserveAspectRatio="none">
  <path d="M0 20 L80 24 L160 16 L240 26 L330 18 L420 28 L510 14 L600 24 L690 18 L780 26 L870 12 L960 22 L1050 10 L1130 18 L1200 0 L1200 531 L0 531 Z" fill="var(--footer)"/>
</svg>
<div class="news-title abs">Sign up for newsletter</div>
<div class="news-sub abs">Excepteur sint occaecat cupidatat non proident, sunt in culpa qui</div>
<div class="news-input abs">Enter email</div>
<div class="news-btn abs">SUBSCRIPTION</div>
<span class="soc abs" style="left:952px;top:3232px"></span>
<span class="soc abs" style="left:992px;top:3232px"></span>
<span class="soc abs" style="left:1032px;top:3232px"></span>
<span class="soc abs" style="left:972px;top:3264px"></span>
<span class="soc abs" style="left:1012px;top:3264px"></span>

<div class="f-head abs" style="left:132px">About Tobin Life</div>
<p class="f-about abs">Sed ut perspiciatis unde omnis iste natus error sit voluptatem accusantium doloremque laudantium, totam rem aperiam, eaque ipsa quae ab illo inventore veritatis et quasi architecto beatae vitae dicta sunt explicabo. Nemo enim ipsam voluptatem quia voluptas sit aspernatur aut odit aut fugit, sed quia consequuntur magni dolores eos qui ratione voluptatem sequi nesciunt. Neque porro quisquam est, qui dolorem ipsum quia dolor sit amet, consectetur, adipisci</p>

<div class="f-head abs" style="left:690px">Contact us</div>
<ul class="f-contact abs">
  <li><svg width="12" height="16" viewBox="0 0 12 16"><path d="M6 0a6 6 0 0 1 6 6c0 4-6 10-6 10S0 10 0 6a6 6 0 0 1 6-6z" fill="#ddd"/><circle cx="6" cy="6" r="2.2" fill="var(--footer)"/></svg><span>Tobin Life<br>Glenhaven, GH4 7TR</span></li>
  <li><svg width="12" height="14" viewBox="0 0 12 14"><path d="M2 0l3 3-1.5 2.5a8 8 0 0 0 4 4L10 8l2 3-2 2.5C5 13 0 8 0 2z" fill="#ddd"/></svg><span>Phone: (480) 555-0142</span></li>
  <li><svg width="14" height="12" viewBox="0 0 14 12"><rect width="14" height="11" fill="#ddd"/><path d="M0 0l7 6 7-6" fill="none" stroke="var(--footer)" stroke-width="1.4"/></svg><span>info@TobinLife.com</span></li>
</ul>

<div class="f-head abs" style="left:956px">Quick links</div>
<ul class="f-links abs">
  <li>Home</li><li>About</li><li>Blog</li><li>Video</li><li>Resources</li><li>Contact</li>
</ul>

<div class="copy abs">Copyright © Tobin Life 2018. All rights reserved.</div>

</body>
</html>
```